Executive retreat/workshop flyer for Harbor Pathway

Our company, Harbor Pathway, runs intensive week long residential retreats for executives suffering from burnout syndrome. We have a programme of therapy which will enable clients to get clarity on what they want out of life and how to achieve it.

Our website is www.harborpathway-example.com. The flyer should have a consistent look and feel to the website. The flyer should be suitable for electronic distribution as well as printing.

The copy should read:

What is it all for? (IN BIG BOLD FONT)

We invite you to The Harbor Pathway

Discover a more meaningful way of being in this world and put passion and purpose back into your life.

Our leading experts will guide you through a holistic program of intellectual, physical, emotional, spiritual and financial work.

You will:

- Draw up a vision of how you want to live your life
- Understand negative behavior loops and how to manage them
- Rebalance relationships which have suffered from stress and neglect
- Examine your attitudes towards money through the Quadrafold System
- Access practical advice on how to implement your goals

Please join us in the beautiful Castlereagh Peninsula this August for a life-changing journey.

This is an intensive program custom tailored to your individual needs. We can only take on a very limited number of participants to maintain intimacy and quality of attention. Book early to avoid disappointment.

Details:

date - mon 27 August - sat 1 sept 2012

Venue- kestrelwood Eco retreat, stony ford, Australia, 1 hour from Melbourne

Price- Special launch offer of US$ 13,860 which is a 30% discount off the normal price of US$ 19,800

10% of profits go to charity

All accommodation, food and individual consultations included.

Please email info@harborpathway-example.com or contact Marnie at 6031 2946

Target Market(s)

Senior executives and leaders mostly with a financial background.

Industry/Entity Type

Residential

Requirements
Must have
• The brochure should look clear in electronic and print format. Can use photos which I've attached.
Nice to have
• Should have a warm, serene feel but appear professional and reliable.

```html
<!DOCTYPE html>
<html lang="en">
<head>
<meta charset="utf-8">
<title>Harbor Pathway – Retreat Flyer</title>
<link rel="stylesheet" href="https://fonts.googleapis.com/css2?family=Cinzel:wght@400;600&family=Source+Sans+3:wght@400;600&display=swap">
<style>
  :root {
    --backdrop: #7d7b2c;
    --paper: #ffffff;
    --plum: #7c2268;
    --plum-dark: #4e1240;
    --olive: #8a8a1f;
    --text-grey: #5f5f63;
    --divider: #d2c6d0;
    --photo-top: #b04ea6;
    --photo-bottom: #93308a;
  }
  * { margin: 0; padding: 0; box-sizing: border-box; }
  html, body { width: 1200px; height: 900px; overflow: hidden; }
  body {
    background: var(--backdrop);
    position: relative;
    font-family: "Source Sans 3", "Myriad Pro", Arial, sans-serif;
    color: var(--text-grey);
  }
  .flyer {
    position: absolute;
    left: 319px; top: 49px;
    width: 578px; height: 808px;
    background: var(--paper);
  }
  .flyer > * { position: absolute; }

  .feature-photo {
    left: 318px; top: 14px;
    width: 248px; height: 228px;
    background: linear-gradient(180deg, var(--photo-top), var(--photo-bottom));
  }
  .divider {
    left: 437px; top: 242px;
    width: 2px; height: 566px;
    background: var(--divider);
  }

  .headline {
    left: 38px; top: 86px;
    font-family: "Cinzel", "Trajan Pro", serif;
    font-weight: 600;
    color: var(--plum);
    font-size: 46px;
    line-height: 48px;
    letter-spacing: -0.5px;
  }
  .headline span { display: block; }
  .headline .line-two { padding-left: 71px; }

  .invite {
    left: 38px; top: 250px;
    font-family: "Cinzel", "Trajan Pro", serif;
    font-weight: 600;
    color: var(--olive);
    font-size: 16.8px;
    letter-spacing: 0.3px;
    white-space: nowrap;
  }

  .lead {
    left: 38px; top: 294px;
    font-size: 15.5px; line-height: 18px;
    white-space: nowrap;
  }
  .intro {
    left: 38px; top: 352px;
    font-size: 13px; line-height: 15px;
    white-space: nowrap;
  }

  .band {
    left: 34px; width: 400px; height: 21px;
    background: linear-gradient(90deg, var(--plum) 0%, var(--plum) 80%, var(--plum-dark) 100%);
    color: #fff;
    font-size: 14px; font-weight: 600;
    line-height: 21px;
    padding-left: 6px;
    letter-spacing: 0.2px;
  }
  .band-outcomes { top: 410px; }
  .band-details { top: 624px; }

  .bullets { list-style: none; }
  .bullets li {
    position: relative;
    padding-left: 24px;
  }
  .bullets li::before {
    content: "";
    position: absolute;
    left: 0; top: 4px;
    width: 16px; height: 6px;
    border-radius: 50%;
    background: var(--olive);
    transform: rotate(-14deg);
  }
  .outcomes {
    left: 34px; top: 441px;
    font-size: 11px; line-height: 16.4px;
  }

  .invitation {
    left: 37px; top: 536px;
    color: var(--olive);
    font-size: 12.3px; font-weight: 600;
    line-height: 14px;
  }
  .note {
    left: 37px; top: 571px;
    width: 350px;
    font-size: 10.4px; line-height: 11px;
  }
  .note span { display: block; text-align: justify; text-align-last: justify; }
  .note span:last-child { text-align-last: left; }

  .details {
    left: 40px; top: 656px;
    font-size: 10.2px; line-height: 11px;
  }
  .details li { margin-bottom: 8px; }
  .details li::before { top: 2px; }
  .details .label { color: var(--olive); font-weight: 600; }
  .details .figure { color: var(--olive); font-size: 13px; }

  .inclusions {
    left: 40px; top: 749px;
    font-size: 9.6px; line-height: 12px;
  }
  .inclusions li::before { background: var(--plum); top: 3px; }

  .charity {
    left: 452px; top: 778px;
    transform-origin: left top;
    transform: rotate(-90deg);
    color: var(--olive);
    font-size: 13.5px;
    white-space: nowrap;
  }
</style>
</head>
<body>
  <main class="flyer">
    <div class="feature-photo" role="img" aria-label="Photograph of a purple allium flower on a long stem"></div>
    <div class="divider"></div>

    <h1 class="headline"><span>What is it</span><span class="line-two">all for?</span></h1>

    <h2 class="invite">We invite you to The Harbor Pathway</h2>

    <p class="lead">Discover a more meaningful way of being in this world<br>and put passion and purpose back into your life.</p>
    <p class="intro">Our leading experts will guide you through a holistic program<br>of intellectual, physical, emotional, spiritual and financial work.</p>

    <h3 class="band band-outcomes">YOU WILL:</h3>
    <ul class="bullets outcomes">
      <li>Draw up a vision of how you want to live your life</li>
      <li>Understand negative behavior loops and how to manage them</li>
      <li>Rebalance relationships which have suffered from stress and neglect</li>
      <li>Examine your attitudes towards money through the Quadrafold System</li>
      <li>Access practical advice on how to implement your goals</li>
    </ul>

    <p class="invitation">Please join us in the beautiful Castlereagh Peninsula this August<br>for a life-changing journey.</p>
    <p class="note"><span>This is an intensive program custom tailored to your individual needs. We</span><span>can only take on a very limited number of participants to maintain</span><span>intimacy and quality of attention. Book early to avoid disappointment.</span></p>

    <h3 class="band band-details">DETAILS:</h3>
    <ul class="bullets details">
      <li><span class="label">DATE:</span> mon 27 August - sat 1 sept 2012</li>
      <li><span class="label">VENUE:</span> kestrelwood Eco retreat, stony ford, Australia,<br>1 hour from Melbourne</li>
      <li><span class="label">PRICE:</span> special launch offer of US$ <span class="figure">13,860</span> which is a <span class="figure">30%</span> discount<br>off the normal price of US$ 19,800</li>
    </ul>

    <ul class="bullets inclusions">
      <li>All accommodation, food and individual consultations included.<br>Please email info@harborpathway-example.com or contact Marnie at 6031 2946</li>
    </ul>

    <p class="charity">10% of profits go to charity</p>
  </main>
</body>
</html>
```